I would love for my business card to be fun and sophisicated. The clients are people that could afford nice well crafted wigs. These wigs are not like granny wigs. The're for women who are stylish and what to look there best especially if they are dealing with cancer are some from of hair loss. Do not want the card to appear crowded with to much information. If I need to eliminate some data, let me know.
Thanks

Industry/Entity Type

Hair

Contact Information for Business Card

L Radiant Tresses, Marjorie Ellison, owner, stylist

Wigs/Studio Showroom
Extensions
Hair Replacement
Private Room

24683 Mesa Vista Loop, Suite. R
Irvine, CA 90871
(949) 555-0178
Email: tresses@lradianttresses-example.com
www.lradianttresses-example.com

```html
<!DOCTYPE html>
<html lang="en">
<head>
<meta charset="utf-8">
<title>L Radiant Tresses – Business Card</title>
<link rel="stylesheet" href="https://fonts.googleapis.com/css2?family=Questrial&display=swap">
<style>
  :root {
    --red: #e8343a;
    --black: #0b0b0b;
    --white: #ffffff;
    --silver-light: #ffffff;
    --silver-dark: #d9d9d9;
    --page: #f3f3f3;
    --hair-dark: #2a1a14;
    --hair-mid: #5a3a2c;
    --skin: #9a6a55;
  }
  * { box-sizing: border-box; margin: 0; padding: 0; }
  html, body {
    width: 1200px; height: 900px; overflow: hidden;
    background: var(--page);
    font-family: "Questrial", "Century Gothic", sans-serif;
  }
  .card {
    position: absolute; left: 100px; top: 160px;
    width: 1000px; height: 580px;
    border-radius: 40px; overflow: hidden;
    box-shadow: 0 10px 30px rgba(0,0,0,0.18);
  }
  .card-shapes { position: absolute; inset: 0; }
  .brand-name {
    position: absolute; left: 240px; top: 80px;
    font-size: 56px; line-height: 1; color: var(--red); letter-spacing: 1px;
    white-space: nowrap;
  }
  .product-photo {
    position: absolute; left: 800px; top: 45px;
    width: 150px; height: 390px;
    border-radius: 70px 70px 20px 20px;
    background: linear-gradient(90deg, var(--hair-dark) 0%, var(--hair-mid) 25%, var(--skin) 50%, var(--hair-mid) 75%, var(--hair-dark) 100%);
  }
  .owner { position: absolute; left: 55px; top: 232px; }
  .owner-name { font-size: 30px; line-height: 34px; color: var(--red); font-weight: 700; }
  .owner-role { font-size: 24px; line-height: 30px; color: var(--white); margin-top: 4px; }
  .contact-list {
    position: absolute; left: 55px; top: 330px;
    list-style: none; color: var(--white); font-size: 24px; line-height: 32px;
  }
  .contact-list li { display: flex; align-items: flex-start; gap: 10px; }
  .contact-list svg { width: 24px; height: 24px; margin-top: 4px; flex: none; fill: var(--red); }
  .services-line {
    position: absolute; left: 55px; bottom: 26px;
    font-size: 20px; line-height: 24px; color: var(--red); white-space: nowrap; letter-spacing: 0.5px;
  }
</style>
</head>
<body>
  <div class="card">
    <svg class="card-shapes" viewBox="0 0 1000 580" width="1000" height="580" aria-hidden="true">
      <defs>
        <linearGradient id="silver" x1="0" y1="0" x2="0" y2="1">
          <stop offset="0" stop-color="var(--silver-dark)"/>
          <stop offset="0.6" stop-color="var(--silver-light)"/>
        </linearGradient>
      </defs>
      <rect width="1000" height="580" fill="url(#silver)"/>
      <path d="M0,125 C250,210 600,270 820,305 C920,325 975,380 1000,430 L1000,580 L0,580 Z" fill="var(--black)"/>
      <path d="M0,30 C90,150 340,240 570,282 C330,225 120,160 0,105 Z" fill="var(--red)"/>
    </svg>

    <div class="brand-name">L Radiant Tresses</div>

    <div class="product-photo" role="img" aria-label="Photo of a long dark brown wig styled on a display head"></div>

    <div class="owner">
      <p class="owner-name">Marjorie Ellison</p>
      <p class="owner-role">owner</p>
    </div>

    <ul class="contact-list">
      <li>
        <svg viewBox="0 0 24 24"><path d="M6.6 10.8a15 15 0 0 0 6.6 6.6l2.2-2.2a1 1 0 0 1 1-.25 11.4 11.4 0 0 0 3.6.57 1 1 0 0 1 1 1V20a1 1 0 0 1-1 1A17 17 0 0 1 3 4a1 1 0 0 1 1-1h3.5a1 1 0 0 1 1 1c0 1.25.2 2.45.57 3.6a1 1 0 0 1-.25 1z"/></svg>
        <span>(949) 555-0178</span>
      </li>
      <li>
        <svg viewBox="0 0 24 24"><path d="M12 2a10 10 0 1 0 0 20 10 10 0 0 0 0-20zm0 2c.9 1.1 1.7 2.6 2.1 4H9.9c.4-1.4 1.2-2.9 2.1-4zM4.3 14a8 8 0 0 1 0-4h3.4a16 16 0 0 0 0 4zm.8 2h3c.3 1.3.8 2.5 1.4 3.5A8 8 0 0 1 5.1 16zm3-8h-3a8 8 0 0 1 4.4-3.5C7.9 5.5 7.5 6.7 8.1 8zM12 20c-.9-1.1-1.700-2.6-2.1-4h4.2c-.4 1.4-1.2 2.9-2.1 4zm2.3-6H9.7a14 14 0 0 1 0-4h4.6a14 14 0 0 1 0 4zm.2 5.5c.6-1 1.1-2.2 1.4-3.5h3a8 8 0 0 1-4.4 3.5zm1.8-5.5a16 16 0 0 0 0-4h3.4a8 8 0 0 1 0 4z"/></svg>
        <span>www.lradianttresses-example.com</span>
      </li>
      <li>
        <svg viewBox="0 0 24 24"><path d="M2 5h20v14H2zm2 2v.5l8 5 8-5V7zm0 2.8V17h16V9.8l-8 5z"/></svg>
        <span>tresses@lradianttresses-example.com</span>
      </li>
      <li>
        <svg viewBox="0 0 24 24"><path d="M12 3 1 12h3v9h6v-6h4v6h6v-9h3z"/></svg>
        <span>Private Room 24683 Mesa Vista Loop,<br>Suite. R Irvine, CA 90871</span>
      </li>
    </ul>

    <p class="services-line">Marjorie Ellison, owner, stylist Wigs/Studio Showroom Extensions Hair Replacement</p>
  </div>
</body>
</html>
```